Business Card: RW Office Partners - Your tidy answer finder

Business Name: RW Office Partners
Website: www.rwofficepartners.com.au
Email: marisol@rwofficepartners.com.au
Mobile: 61 487 902 346
Facebook: @rwofficepartners
Instrgram: @rwofficepartners

Brading Colours:
HEX
#986474
#ddccd3
#7a8498
#c9d8e4
#000000
#ffffff

Tag Line: Your tidy answer finder

Link to DRAFT website:
https://helpdeskhub.sitebuilderx.com/rw-office-partners

About Page from the website:
My name is Marisol Bramwell, and I would love to assist you to become more productive in your day to day and achieve your business and personal goals.
My mission is to give you time, time to work on the important tasks of your business or to be able to spend more time with your family. I will take on the tasks you don’t have time for, don’t know well or simply don’t like to do.
I have an extensive background in Administration, Tender Coordination, Document Control, WHS and Quality Management working primarily in the Construction, Mining and Corporate World.
I am passionate about being organised, having order and making things in your life (and mine) easier! I love to watch something unfold and grow into something amazing! I am known for being the go-to problem solver, the organiser of all things, producing high standards of work even under pressure. I’m also a confident communicator, and I understand that you’re busy running your business.

Target Market(s)

Small to Medium Business who require assistance in their business by a virtual assistant.

Industry/Entity Type

Virtual Assistant

Contact Information for Business Card

Mobile: 61 487 902 346

Font styles to use
Sans Serif

Colors
ffffff

Requirements
Must have
• Branding Colours as outlined.
Contact Details as outlined.
Logo as provided.
Proper contact details - mobile, facebook, instragm, website.
Simple, Elegant, very clean looking.
Should not have
• Note cute with pictures.
Not too girly as still want to market to construction companies.

```html
<!DOCTYPE html>
<html lang="en">
<head>
<meta charset="utf-8">
<title>RW Office Partners – Business Card</title>
<link rel="stylesheet" href="https://fonts.googleapis.com/css2?family=Arimo:wght@400;500&display=swap">
<style>
  :root {
    --mauve: #986474;
    --mauve-soft: #ddccd3;
    --slate: #7a8498;
    --slate-band: #808a9c;
    --sky: #c9d8e4;
    --ink: #3a3a3a;
    --paper: #ffffff;
  }
  * { box-sizing: border-box; margin: 0; padding: 0; }
  html, body {
    width: 1200px;
    height: 1200px;
    overflow: hidden;
    background: var(--paper);
    font-family: "Arimo", Arial, sans-serif;
  }
  .presentation {
    position: relative;
    width: 1200px;
    height: 1200px;
    border: 1px solid var(--ink);
    background: var(--paper);
  }
  .card {
    position: absolute;
    left: 153px;
    top: 331px;
    width: 869px;
    height: 511px;
    border: 1px solid var(--ink);
    background: var(--paper);
    overflow: hidden;
  }
  .card__name-field {
    position: absolute;
    top: 54px;
    left: 0;
    width: 100%;
    text-align: center;
    font-size: 30px;
    color: var(--slate);
    letter-spacing: 0.2px;
  }
  .brand {
    position: absolute;
    top: 195px;
    left: 224px;
    width: 422px;
    text-align: center;
  }
  .brand__name {
    display: block;
    font-size: 44px;
    font-weight: 500;
    line-height: 80px;
    color: var(--slate);
    letter-spacing: 0.5px;
  }
  .brand__rule {
    height: 0;
    border-top: 1.5px solid var(--slate);
    margin-top: 8px;
  }
  .brand__tagline {
    margin-top: 6px;
    font-size: 29px;
    color: var(--slate);
    white-space: nowrap;
  }
  .card__band {
    position: absolute;
    left: 0;
    bottom: 0;
    width: 100%;
    height: 100%;
  }
  .card__band .band-slate { fill: var(--slate-band); }
  .card__band .band-mauve { fill: var(--mauve); }
</style>
</head>
<body>
  <main class="presentation">
    <section class="card" aria-label="RW Office Partners business card, front">
      <p class="card__name-field">Your Name:</p>

      <div class="brand">
        <span class="brand__name">RW Office Partners</span>
        <div class="brand__rule"></div>
        <p class="brand__tagline">Your tidy answer finder</p>
      </div>

      <svg class="card__band" viewBox="0 0 1088 639" preserveAspectRatio="none" aria-hidden="true">
        <path class="band-slate" d="M0 564 H763 C800 564 830 584 841 606 L855 639 H0 Z"/>
        <path class="band-mauve" d="M855 639 L868 610 C880 584 912 564 948 564 H1088 V639 Z"/>
      </svg>
    </section>
  </main>
</body>
</html>
```